Young Architect Bussiness Card

English is not my first language (spanish is).
Need a bussiness card design for my best friend who is about to graduate from college, Licentiate degree in architecture, so she needs business cards to start networking, currently she has no porfolio, web page or facebook. so she is relying on her cel phone and gmail, but should leave space for one of them (facebook)

Design for business card should be modern, maybe something with construction blue prints patern or 3D modelling.

Name: Mariela Ocampo Valverde
Licentiate in Arquitecture
Cel: (506) XXX-8270
email: marielaXXX@correonube.net

Services, although im not sure if it has to be there or not:
Anteproyectos / Proposal design
Inspecciones / Site Inspections
Modelado 3D / 3D modelling
Planos Constructivos / Construction Blue Prints
Presupuestos / Budgets

Design should be in spanish

Industry/Entity Type

Architect

Contact Information for Business Card

Name: Mariela Ocampo, Arquitecto
Associtation code : XXXX
Phone: (506) XXXX-XXXX
Email: xxx@correonube.net
Facebook: xxxx

Requirements
Must have
• Design for business card should be modern, maybe something with construction blue prints patern or 3D modelling.
Nice to have
• Something like a transition from 2D to 3D.

```html
<!DOCTYPE html>
<html lang="es">
<head>
<meta charset="utf-8">
<title>Mariela Ocampo Valverde · Tarjeta de presentación</title>
<link rel="stylesheet" href="https://fonts.googleapis.com/css2?family=Karla:wght@400;500&display=swap">
<style>
  :root {
    --page: #ecebe8;
    --orange: #f2852f;
    --orange-shade: #cc6f2a;
    --graphite: #5e5e60;
    --paper: #ffffff;
    --ink-grey: #5a5a5a;
    --fold-yellow: #f7c21c;
    --text-light: #ffffff;
    --text-dark: #3a3a3a;
  }
  html, body {
    margin: 0;
    padding: 0;
    width: 1200px;
    height: 1200px;
    overflow: hidden;
    background: var(--page);
    font-family: "Karla", Arial, sans-serif;
  }
  .canvas {
    position: relative;
    width: 1200px;
    height: 1200px;
  }
  .card {
    position: absolute;
    left: 190px;
    width: 820px;
    height: 490px;
    overflow: hidden;
    box-shadow: 0 6px 18px rgba(0,0,0,0.18);
  }
  /* Front */
  .card--front {
    top: 80px;
    background: var(--orange);
  }
  .front-shadow {
    position: absolute;
    inset: 0;
  }
  .name-label {
    position: absolute;
    left: 150px;
    top: 165px;
    width: 520px;
    height: 155px;
    background: var(--paper);
    box-sizing: border-box;
    padding: 48px 46px 0 54px;
  }
  .name-label__name {
    margin: 0;
    font-size: 36px;
    font-weight: 400;
    color: var(--orange);
    letter-spacing: 0.5px;
    white-space: nowrap;
  }
  .name-label__title {
    margin: 2px 0 0;
    text-align: right;
    padding-right: 80px;
    font-size: 22px;
    color: var(--ink-grey);
  }
  /* Back */
  .card--back {
    top: 630px;
    background: var(--graphite);
  }
  .services-note {
    position: absolute;
    left: 47px;
    top: 47px;
    width: 298px;
    height: 298px;
  }
  .services-note svg {
    position: absolute;
    inset: 0;
  }
  .services-list {
    position: absolute;
    left: 22px;
    top: 22px;
    margin: 0;
    padding: 0;
    list-style: none;
    font-size: 24px;
    color: var(--text-dark);
  }
  .services-list li {
    height: 52px;
    line-height: 36px;
  }
  .contact {
    position: absolute;
    right: 48px;
    bottom: 40px;
    margin: 0;
    text-align: right;
    font-size: 24px;
    line-height: 31px;
    color: var(--text-light);
    font-style: normal;
  }
</style>
</head>
<body>
<main class="canvas">
  <section class="card card--front" aria-label="Frente de la tarjeta">
    <svg class="front-shadow" width="820" height="490" viewBox="0 0 820 490" aria-hidden="true">
      <polygon points="150,165 -450,765 70,920 670,320" fill="var(--orange-shade)"/>
    </svg>
    <div class="name-label">
      <h1 class="name-label__name">Mariela Ocampo Valverde</h1>
      <p class="name-label__title">Arquitecto</p>
    </div>
  </section>

  <section class="card card--back" aria-label="Reverso de la tarjeta">
    <div class="services-note">
      <svg width="298" height="298" viewBox="0 0 298 298" aria-hidden="true">
        <polygon points="0,0 298,0 298,252 252,298 0,298" fill="var(--orange)"/>
        <polygon points="252,298 298,252 240,270" fill="rgba(0,0,0,0.18)"/>
        <polygon points="252,298 298,252 246,256" fill="var(--fold-yellow)"/>
      </svg>
      <ul class="services-list">
        <li>Anteproyectos</li>
        <li>Inspecciones</li>
        <li>Modelado 3D</li>
        <li>Planos Constructivos</li>
        <li>Presupuestos</li>
      </ul>
    </div>
    <address class="contact">
      Assocition code : XXXX<br>
      Phone: (506) XXXX-XXXX<br>
      Email: marielaXXX@correonube.net<br>
      Facebook: xxxx
    </address>
  </section>
</main>
</body>
</html>
```